Letterhead for Business Law Firm

We need a letter head for our firm based on the design we have settled on and it is attached. Our clients are small and large businesses around the world, and our letterhead is used typically for formal legal purposes such as demand letters (accusing the recipient of doing bad things) or responding to demand letters. It may also be sent to regulators and other government agencies. So this needs to be tasteful, but a little edgy as well - we try to convey that we are a firm that is different - businesses and investors come to us for creative, quick advice, typically in high stress circumstances, and for our ability to work through high conflict situations, and rapid paced engagements.

Target Market(s)

Lawyers, business executives, investors, government regulators who may receive letters from this firm on behalf of its clients.

Industry/Entity Type

Business

Requirements
Must have
• The design and the firm's contact information:
• Thornvale Law Firm, P.C.
• 8172 SW 17th Ave
• Portland, OR 97058
• phone: 971 555 0147
• fax: 971 555 0182
• in what placement and how depicted (e.g. a phone icon instead of the word "phone") I leave to your creative ideas.
Nice to have
• design and information can be placed at the top, bottom and/or sides of the letter, and the design should be for a standard letter size paper - and can have a separate design for the second page.

```html
<!DOCTYPE html>
<html lang="en">
<head>
<meta charset="utf-8">
<title>Thornvale Letterhead</title>
<link href="https://fonts.googleapis.com/css2?family=Arimo:wght@400;700&display=swap" rel="stylesheet">
<style>
  :root {
    --teal: #4a7378;
    --teal-light: #9db8bb;
    --ink: #231f20;
    --paper: #ffffff;
  }
  html, body { margin: 0; padding: 0; overflow: hidden; background: var(--paper); }
  .letterhead {
    position: relative;
    width: 928px;
    height: 1200px;
    overflow: hidden;
    background: var(--paper);
    font-family: "Arimo", Arial, sans-serif;
    color: var(--ink);
  }
  .brand {
    position: absolute;
    left: 22px;
    top: 22px;
    height: 60px;
    display: flex;
    align-items: center;
    gap: 12px;
  }
  .brand-mark { width: 22px; height: 22px; background: var(--teal); }
  .brand-name {
    font-size: 34px;
    font-weight: 400;
    letter-spacing: 8px;
    color: var(--ink);
  }
  .contact { position: absolute; inset: 0; font-size: 13px; line-height: 16px; }
  .contact-row { position: absolute; white-space: nowrap; }
  .contact-row svg { position: absolute; }
  .address { left: 571px; top: 32px; }
  .address svg { left: -23px; top: 0; }
  .email { left: 571px; top: 70px; }
  .email svg { left: -25px; top: 1px; }
  .web { left: 571px; top: 88px; font-weight: 700; color: var(--teal); }
  .divider {
    position: absolute;
    left: 752px; top: 30px;
    width: 2px; height: 66px;
    background: var(--teal);
  }
  .phone { left: 800px; top: 35px; }
  .phone svg { left: -23px; top: -3px; }
  .mobile { left: 800px; top: 59px; }
  .mobile svg { left: -20px; top: 0; }
  .fax { left: 768px; top: 82px; }
  .fax .label { color: var(--teal); margin-right: 4px; }
  .footer-wave { position: absolute; left: 0; bottom: 0; width: 928px; height: 100px; display: block; }
  .footer-web {
    position: absolute;
    left: 734px; top: 1148px;
    font-size: 18px;
    color: var(--paper);
  }
</style>
</head>
<body>
<main class="letterhead">
  <header>
    <div class="brand">
      <span class="brand-mark"></span>
      <span class="brand-name">THORNVALE</span>
    </div>

    <div class="contact">
      <div class="contact-row address">
        <svg width="12" height="15" viewBox="0 0 12 15" aria-hidden="true"><path d="M6 0a6 6 0 0 0-6 6c0 4 6 9 6 9s6-5 6-9a6 6 0 0 0-6-6zm0 8.3A2.3 2.3 0 1 1 6 3.7a2.3 2.3 0 0 1 0 4.6z" fill="var(--teal)"/></svg>
        <span>8172 SW 17th Ave,<br>Portland, OR&nbsp; 97058</span>
      </div>
      <div class="contact-row email">
        <svg width="19" height="13" viewBox="0 0 19 13" aria-hidden="true"><rect x="0.5" y="0.5" width="18" height="12" rx="1" fill="var(--teal)"/><path d="M1 1l8.5 6.5L18 1M1 12l6-5M18 12l-6-5" stroke="#fff" stroke-width="1.2" fill="none"/></svg>
        <span>name@thornvale.com</span>
      </div>
      <div class="contact-row web"><span>www.thornvale.com</span></div>

      <div class="divider"></div>

      <div class="contact-row phone">
        <svg width="20" height="20" viewBox="0 0 20 20" aria-hidden="true"><circle cx="10" cy="10" r="9" fill="none" stroke="var(--teal)" stroke-width="1.3"/><path d="M6.5 5.5l2 -.3 1 2.4-1.2 1c.6 1.3 1.5 2.2 2.8 2.8l1-1.2 2.4 1-.3 2c-4.5.3-8-3.2-7.7-7.7z" fill="var(--teal)"/></svg>
        <span>971 555 0147</span>
      </div>
      <div class="contact-row mobile">
        <svg width="10" height="15" viewBox="0 0 10 15" aria-hidden="true"><rect x="0.5" y="0.5" width="9" height="14" rx="1.5" fill="var(--teal)"/><rect x="2" y="2" width="6" height="7" fill="#fff"/><rect x="2" y="10.5" width="6" height="2.5" fill="#fff" opacity=".6"/></svg>
        <span>971 555 0163</span>
      </div>
      <div class="contact-row fax"><span class="label">Fax :</span><span>971 555 0182</span></div>
    </div>
  </header>

  <footer>
    <svg class="footer-wave" viewBox="0 0 928 100" preserveAspectRatio="none" aria-hidden="true">
      <path d="M0 22 C50 28 100 70 240 76 C420 84 650 38 928 30 L928 100 L0 100 Z" fill="var(--teal)"/>
      <path d="M380 70 C600 46 780 28 928 22 L928 31 C700 36 520 60 380 70 Z" fill="var(--teal-light)"/>
      <path d="M60 91 C360 94 640 62 928 44" fill="none" stroke="#fff" stroke-width="2"/>
    </svg>
    <div class="footer-web">www.thornvale.com</div>
  </footer>
</main>
</body>
</html>
```